Software Company Business Card

We are looking for a new design of our business card. The design will also be used in the rest of our branding and marketing materials as we want to keep it all uniform. We sell POS software to fine/luxury jewelers and also offer other business services as well to help the jeweler manage their business and need something more updated, technical and fresh, preferably more on the masculine side. We do not want any designs with gems in them but if possible would like to incorporate the circle and arrow in the logo into the design, but not a requirement if you can't make it work. I would like to see a variety of the mix. The colors need to remain our blue and orange and the logo can not change. The squiggly lines have been used as our corporate identity for over 20 years and its time to update. Our company name is TELK (Summit Counter Operations Platform).

Target Market(s)

High End Jewelers

Industry/Entity Type

Software

Contact Information for Business Card

Requirements
Must have
• Our logo and the colors must remain the same. Blue is #d95d39 and Orange is #0f5682.
Nice to have
• The circle and arrow incorporated but not a requirement.
Should not have
• Anything jewelry or gem related.

```html
<!DOCTYPE html>
<html lang="en">
<head>
<meta charset="utf-8">
<title>TELK Business Card</title>
<link href="https://fonts.googleapis.com/css2?family=Montserrat:wght@400;600;800&display=swap" rel="stylesheet">
<style>
  :root {
    --brand-blue: #065585;
    --brand-orange: #d95d39;
    --text-grey: #575757;
    --paper: #ffffff;
    --backdrop: #dadada;
    --emboss: #0a2f47;
  }
  html, body {
    margin: 0;
    width: 1200px;
    height: 1200px;
    overflow: hidden;
    background: var(--backdrop);
    font-family: "Montserrat", sans-serif;
  }
  .card {
    position: absolute;
    left: 220px;
    width: 768px;
    height: 439px;
    overflow: hidden;
  }
  .card-front { top: 116px; background: var(--paper); }
  .card-back { top: 652px; background: var(--brand-blue); }

  .card-wave { position: absolute; inset: 0; }

  .brand-lockup {
    position: absolute;
    display: flex;
    align-items: center;
  }
  .brand-name {
    font-weight: 800;
    line-height: 1;
    letter-spacing: -1px;
  }
  .brand-dot { border-radius: 50%; }

  .card-front .brand-lockup { left: 49px; top: 184px; gap: 22px; }
  .card-front .brand-name { font-size: 68px; color: var(--brand-blue); }
  .card-front .brand-dot { width: 66px; height: 66px; background: var(--brand-orange); }

  .card-back .brand-lockup { left: 141px; top: 169px; gap: 32px; }
  .card-back .brand-name { font-size: 122px; color: var(--emboss); }
  .card-back .brand-dot { width: 102px; height: 102px; background: var(--emboss); }

  .divider {
    position: absolute;
    left: 394px;
    top: 87px;
    width: 2px;
    height: 263px;
    background: var(--brand-orange);
  }
  .contact {
    position: absolute;
    left: 427px;
    top: 82px;
    color: var(--text-grey);
    font-size: 18.5px;
    line-height: 24.5px;
  }
  .contact-name {
    margin: 0;
    font-size: 30px;
    line-height: 34px;
    font-weight: 600;
    color: var(--brand-blue);
  }
  .contact-title { margin: 0 0 11px; }
  .contact-address { margin: 0 0 8px; font-style: normal; }
  .contact-list { list-style: none; margin: 0; padding: 0; }
  .contact-list li { display: flex; align-items: center; gap: 8px; }
  .contact-list svg { width: 14px; height: 14px; flex: none; }
  .web-strong { color: var(--brand-blue); font-weight: 600; }
</style>
</head>
<body>

<section class="card card-front">
  <svg class="card-wave" viewBox="0 0 768 439" preserveAspectRatio="none" aria-hidden="true">
    <path d="M0 344 C180 420 420 425 600 414 C680 409 740 398 768 388 L768 439 L0 439 Z" fill="var(--brand-blue)"/>
    <path d="M118 376 C300 412 560 412 768 362 L768 382 C560 420 320 418 118 376 Z" fill="var(--brand-orange)"/>
  </svg>

  <div class="brand-lockup">
    <span class="brand-name">TELK</span>
    <span class="brand-dot"></span>
  </div>

  <div class="divider"></div>

  <div class="contact">
    <h1 class="contact-name">Desmond Ravell</h1>
    <p class="contact-title">Director of Global Operations</p>
    <address class="contact-address">
      1480 Meridian Parkway<br>
      Suite 210<br>
      Carver, NV 89120<br>
      USA
    </address>
    <ul class="contact-list">
      <li>
        <svg viewBox="0 0 14 14"><path d="M3 1 L5 1 L6 4 L4.5 5 C5 7 7 9 9 9.5 L10 8 L13 9 L13 11 C13 12 12 13 11 13 C6 12.5 1.5 8 1 3 C1 2 2 1 3 1 Z" fill="var(--brand-orange)"/></svg>
        +1 555 204-7731
      </li>
      <li>
        <svg viewBox="0 0 14 14"><rect x="3.5" y="1" width="7" height="4" fill="var(--brand-orange)"/><rect x="1" y="5" width="12" height="5" rx="1" fill="var(--brand-orange)"/><rect x="3.5" y="8.5" width="7" height="4.5" fill="var(--brand-orange)" stroke="#fff" stroke-width="1"/></svg>
        +1 555 318-6042
      </li>
      <li>
        <svg viewBox="0 0 14 14"><rect x="1.5" y="3" width="11" height="8" fill="none" stroke="var(--brand-orange)" stroke-width="1.5"/><path d="M1.5 3 L7 7.5 L12.5 3" fill="none" stroke="var(--brand-orange)" stroke-width="1.5"/></svg>
        desmond@telkusa.com
      </li>
      <li>
        <svg viewBox="0 0 14 14" fill="none" stroke="var(--brand-orange)" stroke-width="1"><circle cx="7" cy="7" r="5.8"/><ellipse cx="7" cy="7" rx="2.6" ry="5.8"/><path d="M1.2 7 H12.8 M2 4 H12 M2 10 H12"/></svg>
        <span>www.<span class="web-strong">telkusa</span>.com</span>
      </li>
    </ul>
  </div>
</section>

<section class="card card-back">
  <div class="brand-lockup">
    <span class="brand-name">TELK</span>
    <span class="brand-dot"></span>
  </div>
</section>

</body>
</html>
```